Business Card for a Wedding Films Business

We require a business card design for our business 'Lewis Marrow Wedding Films'. The logo needs to look classy and high end.

Target Market(s)

Wedding Couples

Contact Information for Business Card

Lewis Marrow Wedding Films
07312 605 227
films@lewismarrowreels.com
www.lewismarrowreels.com

Facebook: @lewismarrowweddingfilms
Instagram: @lewismarrowfilms

Font styles to use
Sans Serif

Requirements
Must have
• Social media icons - Facebook and Instagram

```html
<!DOCTYPE html>
<html lang="en">
<head>
<meta charset="utf-8">
<title>Lewis Marrow Wedding Films – Business Card</title>
<link href="https://fonts.googleapis.com/css2?family=Jost:wght@400;500&display=swap" rel="stylesheet">
<style>
  :root{
    --ink:#000000;
    --paper:#ffffff;
    --rule:#3a3a3a;
    --text-dark:#111111;
  }
  *{margin:0;padding:0;box-sizing:border-box;}
  html,body{width:750px;height:1200px;overflow:hidden;background:var(--paper);}
  body{position:relative;font-family:'Jost',sans-serif;}

  .card{position:absolute;left:113px;width:525px;height:300px;overflow:hidden;}
  .card--front{top:41px;background:var(--paper);border:1px solid var(--rule);}
  .card--back{top:370px;background:var(--ink);}

  .front-panel{position:absolute;inset:0;}

  .brand{position:absolute;text-align:center;font-weight:500;text-transform:uppercase;}
  .brand__name{display:block;letter-spacing:0.16em;}
  .brand__tag{display:block;letter-spacing:0.38em;}

  .card--front .brand{color:var(--text-dark);left:290px;width:230px;top:95px;}
  .card--front .brand__name{font-size:19px;}
  .card--front .brand__tag{font-size:9px;margin-top:4px;}

  .contact{position:absolute;left:27px;top:132px;color:var(--paper);list-style:none;}
  .contact__company{font-size:12px;margin-bottom:12px;}
  .contact__item{display:flex;align-items:center;gap:8px;font-size:12.5px;height:18px;}
  .contact__item--gap{margin-top:17px;}
  .contact__icon{width:11px;height:11px;flex:none;}

  .card--back .brand{color:var(--paper);left:0;width:100%;top:148px;}
  .card--back .brand__name{font-size:24px;}
  .card--back .brand__tag{font-size:11px;margin-top:4px;}

  .web-band{position:absolute;left:0;top:228px;width:100%;height:25px;background:var(--paper);
    display:flex;align-items:center;justify-content:center;}
  .web-band__text{font-size:12.5px;letter-spacing:0.62em;color:var(--text-dark);padding-left:0.62em;}
</style>
</head>
<body>

<section class="card card--front">
  <svg class="front-panel" width="525" height="300" viewBox="0 0 525 300" aria-hidden="true">
    <polygon points="0,0 175,0 347,300 0,300" fill="#000"/>
  </svg>

  <div class="brand">
    <span class="brand__name">Lewis Marrow</span>
    <span class="brand__tag">Wedding Films</span>
  </div>

  <ul class="contact">
    <li class="contact__company">Lewis Marrow Wedding Films</li>
    <li class="contact__item">
      <svg class="contact__icon" viewBox="0 0 24 24"><path fill="#fff" d="M6.6 10.8c1.4 2.8 3.8 5.1 6.6 6.6l2.2-2.2c.3-.3.7-.4 1-.2 1.1.4 2.3.6 3.6.6.6 0 1 .4 1 1V20c0 .6-.4 1-1 1C10.6 21 3 13.4 3 4c0-.6.4-1 1-1h3.5c.6 0 1 .4 1 1 0 1.2.2 2.4.6 3.6.1.3 0 .7-.2 1z"/></svg>
      07312 605 227
    </li>
    <li class="contact__item">
      <svg class="contact__icon" viewBox="0 0 24 24"><rect x="2" y="5" width="20" height="14" fill="none" stroke="#fff" stroke-width="2"/><path d="M2 5l10 8 10-8" fill="none" stroke="#fff" stroke-width="2"/></svg>
      films@lewismarrowreels.com
    </li>
    <li class="contact__item">
      <svg class="contact__icon" viewBox="0 0 24 24"><circle cx="12" cy="12" r="10" fill="#fff"/><path d="M7 8c2 0 3 1 3 3s-2 2-1 4M15 5c-1 2 1 3 3 3M14 19c0-2 1-3 3-3" fill="none" stroke="#000" stroke-width="1.6"/></svg>
      www.lewismarrowreels.com
    </li>
    <li class="contact__item contact__item--gap">
      <svg class="contact__icon" viewBox="0 0 24 24"><rect x="2" y="2" width="20" height="20" rx="3" fill="#fff"/></svg>
      lewismarrowweddingfilms
    </li>
    <li class="contact__item">
      <svg class="contact__icon" viewBox="0 0 24 24"><circle cx="12" cy="12" r="9" fill="none" stroke="#fff" stroke-width="2.4"/></svg>
      lewismarrowfilms
    </li>
  </ul>
</section>

<section class="card card--back">
  <div class="brand">
    <span class="brand__name">Lewis Marrow</span>
    <span class="brand__tag">Wedding Films</span>
  </div>
  <div class="web-band">
    <span class="web-band__text">WWW.LEWISMARROWREELS.COM</span>
  </div>
</section>

</body>
</html>
```